Maple Ridge business card design

Card needs to include the following text/items:
Company Logo
Tobin Marsh
Phone # - 555-318-7642
service@mapleridgelandscaping.example
Lawn & landscape maintenance services

```html
<!DOCTYPE html>
<html lang="en">
<head>
<meta charset="utf-8">
<title>Maple Ridge Landscaping – Business Card</title>
<link href="https://fonts.googleapis.com/css2?family=Cinzel:wght@700&family=Roboto+Condensed:wght@400;500&display=swap" rel="stylesheet">
<style>
  :root {
    --backdrop: #3d7589;
    --sky-top: #6fcdf0;
    --sky-bottom: #e6f6fc;
    --brand-green: #1f5233;
    --ink: #1b1b1b;
    --grass-dark: #2f6d1f;
    --grass-light: #6fb43a;
    --mark-fill: #3f7d45;
  }
  * { box-sizing: border-box; margin: 0; padding: 0; }
  html, body { width: 1200px; height: 1200px; overflow: hidden; }
  body { background: var(--backdrop); position: relative; }

  .card {
    position: absolute;
    top: 461px;
    width: 486px;
    height: 277px;
    overflow: hidden;
    background: linear-gradient(180deg, var(--sky-top) 0%, #a9e1f5 60%, var(--sky-bottom) 100%);
  }
  .card--front { left: 83px; }
  .card--back { left: 632px; }

  .grass { position: absolute; left: 0; bottom: 0; width: 100%; height: 80px; display: block; }

  .brand { position: absolute; text-align: center; color: var(--brand-green); }
  .brand__mark { display: block; margin: 0 auto; border-radius: 50%; background: var(--mark-fill); }
  .brand__name { font-family: "Cinzel", serif; font-weight: 700; line-height: 1; white-space: nowrap; }
  .brand__sub { font-family: "Cinzel", serif; font-weight: 700; line-height: 1; white-space: nowrap; }

  .card--front .brand { left: 206px; top: 28px; width: 270px; }
  .card--front .brand__mark { width: 178px; height: 178px; }
  .card--front .brand__name { font-size: 34px; margin-top: 10px; }
  .card--front .brand__sub { font-size: 13px; letter-spacing: 15px; margin-top: 4px; margin-right: -15px; }

  .card--back .brand { left: 296px; top: 49px; width: 176px; }
  .card--back .brand__mark { width: 118px; height: 118px; }
  .card--back .brand__name { font-size: 22px; margin-top: 4px; }
  .card--back .brand__sub { font-size: 9px; letter-spacing: 9px; margin-top: 2px; margin-right: -9px; }

  .person { position: absolute; left: 21px; top: 34px; }
  .person__name { font-family: "Cinzel", serif; font-weight: 700; font-size: 33px; color: var(--brand-green); line-height: 1; }
  .person__role { font-family: "Roboto Condensed", sans-serif; font-weight: 500; font-size: 12px; color: var(--ink); letter-spacing: 0.5px; margin-top: 9px; }

  .contacts { position: absolute; left: 22px; top: 113px; list-style: none; }
  .contacts__item { display: flex; align-items: center; height: 33px; font-family: "Roboto Condensed", sans-serif; font-size: 14.5px; color: var(--ink); }
  .contacts__icon { width: 19px; height: 19px; margin-right: 9px; flex: none; }
  .contacts__square { width: 18px; height: 18px; margin-right: 9px; background: var(--brand-green); flex: none; }
</style>
</head>
<body>

<section class="card card--front">
  <div class="brand">
    <span class="brand__mark" role="img" aria-label="Maple Ridge emblem"></span>
    <div class="brand__name">Maple Ridge</div>
    <div class="brand__sub">LANDSCAPING</div>
  </div>
  <svg class="grass" viewBox="0 0 486 80" preserveAspectRatio="none" role="img" aria-label="Illustrated grass along the bottom edge">
    <defs>
      <linearGradient id="grass-front" x1="0" y1="0" x2="0" y2="1">
        <stop offset="0" stop-color="var(--grass-light)"/>
        <stop offset="1" stop-color="var(--grass-dark)"/>
      </linearGradient>
    </defs>
    <path d="M0 10 Q90 0 180 20 Q200 40 190 58 L486 58 L486 80 L0 80 Z" fill="url(#grass-front)"/>
  </svg>
</section>

<section class="card card--back">
  <div class="person">
    <div class="person__name">TOBIN MARSH</div>
    <div class="person__role">LAWN &amp; LANDSCAPE MAINTENANCE SERVICES</div>
  </div>

  <ul class="contacts">
    <li class="contacts__item">
      <svg class="contacts__icon" viewBox="0 0 24 24"><path fill="var(--brand-green)" d="M6.6 10.8c1.4 2.8 3.8 5.1 6.6 6.6l2.2-2.2c.3-.3.7-.4 1-.2 1.1.4 2.3.6 3.6.6.6 0 1 .4 1 1V20c0 .6-.4 1-1 1C10.6 21 3 13.4 3 4c0-.6.4-1 1-1h3.5c.6 0 1 .4 1 1 0 1.3.2 2.5.6 3.6.1.3 0 .7-.2 1z"/></svg>
      555-318-7642
    </li>
    <li class="contacts__item">
      <svg class="contacts__icon" viewBox="0 0 24 24" fill="none" stroke="var(--brand-green)" stroke-width="1.8"><circle cx="12" cy="12" r="9"/><ellipse cx="12" cy="12" rx="4" ry="9"/><path d="M3 12h18M4.5 7.5h15M4.5 16.5h15"/></svg>
      mapleridgelandscaping.example
    </li>
    <li class="contacts__item">
      <svg class="contacts__icon" viewBox="0 0 24 24" fill="none" stroke="var(--brand-green)" stroke-width="1.8"><rect x="2.5" y="5" width="19" height="14"/><path d="M2.5 5l9.5 8 9.5-8M2.5 19l7-6.5M21.5 19l-7-6.5"/></svg>
      service@mapleridgelandscaping.example
    </li>
    <li class="contacts__item">
      <span class="contacts__square"></span>
      social.example/mapleridgelandscaping
    </li>
  </ul>

  <div class="brand">
    <span class="brand__mark" role="img" aria-label="Maple Ridge emblem"></span>
    <div class="brand__name">Maple Ridge</div>
    <div class="brand__sub">LANDSCAPING</div>
  </div>

  <svg class="grass" viewBox="0 0 486 80" preserveAspectRatio="none" role="img" aria-label="Illustrated grass along the bottom edge">
    <defs>
      <linearGradient id="grass-back" x1="0" y1="0" x2="0" y2="1">
        <stop offset="0" stop-color="var(--grass-light)"/>
        <stop offset="1" stop-color="var(--grass-dark)"/>
      </linearGradient>
    </defs>
    <path d="M0 58 L305 58 Q300 40 320 25 Q400 5 486 12 L486 80 L0 80 Z" fill="url(#grass-back)"/>
  </svg>
</section>

</body>
</html>
```